Real Estate Business Card

On the front side I want to have my info, my brokerage info.
On the back side I want have my complany’s logo, website and Facebook link. I will provide all this once I select a design.

I would like to see Black background and gold text, Dark Blue and gold text and White and blue text designs

Font styles to use
Sans Serif
Script

```html
<!DOCTYPE html>
<html lang="en">
<head>
<meta charset="utf-8">
<title>Harborline Homes – Business Card</title>
<link rel="stylesheet" href="https://fonts.googleapis.com/css2?family=Cinzel:wght@600&family=PT+Sans:wght@400&display=swap">
<style>
  :root {
    --canvas: #9a9a9a;
    --card-white: #ffffff;
    --brand-blue: #1f47a8;
    --navy-top: #2856b6;
    --navy-bottom: #1b3f8c;
    --gold: #f0c63a;
    --ink: #222428;
    --rule: #dcdcdc;
    --back-text: #dce3f2;
  }
  * { margin: 0; padding: 0; box-sizing: border-box; }
  html, body { width: 1200px; height: 900px; overflow: hidden; }
  body {
    position: relative;
    background: var(--canvas);
    font-family: "PT Sans", Arial, sans-serif;
    color: var(--ink);
  }
  .card { position: absolute; width: 478px; height: 295px; }

  /* Front */
  .card-front {
    left: 120px; top: 275px;
    background: var(--card-white);
    border-radius: 0 48px 0 48px;
  }
  .brand-name {
    position: absolute;
    font-family: "Cinzel", Georgia, serif;
    font-weight: 600;
    text-align: center;
    line-height: 1;
  }
  .card-front .brand-name {
    left: 212px; top: 80px; width: 240px;
    color: var(--brand-blue);
  }
  .brand-main { display: block; font-size: 30px; letter-spacing: 0.5px; }
  .brand-sub { display: block; font-size: 15px; letter-spacing: 6px; margin-top: 8px; }
  .brand-mark {
    position: absolute;
    width: 14px; height: 14px;
    background: var(--brand-blue);
    left: 325px; top: 52px;
  }

  .person-name {
    position: absolute; left: 30px; top: 160px;
    font-family: "Cinzel", Georgia, serif; font-weight: 600;
    font-size: 19px; color: var(--brand-blue); letter-spacing: 0.3px;
  }
  .person-title {
    position: absolute; left: 30px; top: 181px;
    font-size: 13px; color: var(--ink);
  }
  .title-rule {
    position: absolute; left: 148px; top: 189px; width: 296px;
    height: 1px; background: var(--rule);
  }
  .contact-list {
    position: absolute; left: 30px; top: 203px;
    list-style: none; font-size: 13.5px;
  }
  .contact-list li {
    display: flex; align-items: center; height: 17.5px;
  }
  .contact-list svg { width: 10px; height: 10px; margin-right: 5px; fill: var(--brand-blue); }

  .office-info {
    position: absolute; right: 33px; top: 212px;
    text-align: right; font-size: 13px; line-height: 17px;
  }
  .office-web { color: var(--brand-blue); margin-bottom: 6px; }

  /* Back */
  .card-back {
    left: 606px; top: 273px;
    background: linear-gradient(180deg, var(--navy-top), var(--navy-bottom));
    border-radius: 48px 0 48px 0;
  }
  .card-back .brand-name {
    left: 89px; top: 138px; width: 300px;
    color: var(--gold);
  }
  .card-back .brand-main { font-size: 36px; }
  .card-back .brand-sub { font-size: 16px; letter-spacing: 7px; }
  .card-back .brand-mark { background: var(--gold); left: 232px; top: 95px; width: 16px; height: 16px; }
  .back-link {
    position: absolute; left: 0; width: 100%; top: 228px;
    text-align: center; font-size: 14px; color: var(--back-text);
  }
</style>
</head>
<body>
  <section class="card card-front" aria-label="Business card front">
    <span class="brand-mark"></span>
    <div class="brand-name">
      <span class="brand-main">HARBORLINE</span>
      <span class="brand-sub">HOMES</span>
    </div>

    <h1 class="person-name">DANIEL WHITMORE</h1>
    <p class="person-title">Managing Director</p>
    <div class="title-rule"></div>

    <ul class="contact-list">
      <li><svg viewBox="0 0 10 10"><path d="M1 3.2C1 2 2 1.5 5 1.5S9 2 9 3.2L7.6 4 6.8 3H3.2L2.4 4zM2.3 4.6h5.4L9 8.6H1z"/></svg>061-482 730 915</li>
      <li><svg viewBox="0 0 10 10"><path d="M3 0.5h4a.8.8 0 0 1 .8.8v7.4a.8.8 0 0 1-.8.8H3a.8.8 0 0 1-.8-.8V1.3A.8.8 0 0 1 3 .5zM3.2 1.6v5.8h3.6V1.6z"/></svg>061-482 730 915</li>
      <li><svg viewBox="0 0 10 10"><path d="M0.5 2h9v6h-9zM1.3 2.6 5 5.4l3.7-2.8z" fill-rule="evenodd"/></svg>hello@harborline.com</li>
      <li><svg viewBox="0 0 10 10"><circle cx="5" cy="5" r="4.5"/><path d="M3 3.5c1 .2 1.4 1 1 1.8L3 6.3M6.5 2c-.3 1 .5 1.5 1.5 1.4M6 8.3c0-1 .5-1.6 1.6-1.8" stroke="#fff" stroke-width=".8" fill="none"/></svg>www.harborlinehomes.com</li>
    </ul>

    <div class="office-info">
      <p class="office-web">www.harborlinehomes.com</p>
      <p>2178, Quayside Avenue</p>
      <p>Port Elara, 604219</p>
    </div>
  </section>

  <section class="card card-back" aria-label="Business card back">
    <span class="brand-mark"></span>
    <div class="brand-name">
      <span class="brand-main">HARBORLINE</span>
      <span class="brand-sub">HOMES</span>
    </div>
    <p class="back-link">www.harborlinehomes.com/community</p>
  </section>
</body>
</html>
```